Handmade candle business in melbourne requiring assistance with designing classy labels

My business name is Wick and Willow.
I specialise in making handmade candles, i'm based in Melbourne.
My moto is "Delicately hand poured and infused by me...for you"
wickwillow@mailbox-demo.net
0487 913 072

I need some assistance with designing my labels for my glass candles
I really like earthy colours and nothing too bright, but I want it to look classy and elegant and something that stands out from other homemade candle businesses.
I have attached a sample of a design that appeals to me but open to suggestions.

```html
<!DOCTYPE html>
<html lang="en">
<head>
<meta charset="utf-8">
<title>Wick and Willow – Candle Label</title>
<link rel="stylesheet" href="https://fonts.googleapis.com/css2?family=Pinyon+Script&family=Open+Sans:wght@400&display=swap">
<style>
  :root {
    --page: #ffffff;
    --ring-light: #e6d0b1;
    --ring-mid: #c9a684;
    --ring-dark: #a2734f;
    --fill-light: #e4ccab;
    --fill-mid: #d9bd9b;
    --fill-dark: #b9906f;
    --trim-brown: #6a2a0c;
    --trim-copper: #c27019;
    --trim-plum: #3b2142;
    --trim-gold: #b8860b;
    --hairline: #ffffff;
    --ink: #000000;
  }
  html, body {
    margin: 0;
    padding: 0;
    width: 1200px;
    height: 1199px;
    overflow: hidden;
    background: var(--page);
  }
  .label {
    display: block;
    width: 1200px;
    height: 1199px;
  }
  .motto-lead {
    font-family: "Pinyon Script", cursive;
    font-size: 178px;
    fill: var(--ink);
  }
  .motto-line {
    font-family: "Pinyon Script", cursive;
    font-size: 104px;
    fill: var(--ink);
  }
  .email-user {
    font-family: "Open Sans", sans-serif;
    font-size: 118px;
    fill: var(--ink);
  }
  .email-domain {
    font-family: "Open Sans", sans-serif;
    font-size: 46px;
    fill: var(--ink);
  }
  .phone {
    font-family: "Open Sans", sans-serif;
    font-size: 74px;
    fill: var(--ink);
  }
</style>
</head>
<body>
<svg class="label" viewBox="0 0 1200 1199" xmlns="http://www.w3.org/2000/svg" aria-label="Wick and Willow candle label">
  <defs>
    <linearGradient id="ringGradient" x1="0" y1="0" x2="1" y2="0">
      <stop offset="0" style="stop-color: var(--ring-dark)"/>
      <stop offset="0.3" style="stop-color: var(--ring-mid)"/>
      <stop offset="0.5" style="stop-color: var(--ring-light)"/>
      <stop offset="0.72" style="stop-color: var(--ring-mid)"/>
      <stop offset="1" style="stop-color: var(--ring-dark)"/>
    </linearGradient>
    <linearGradient id="fillGradient" x1="0" y1="0" x2="1" y2="0">
      <stop offset="0" style="stop-color: var(--fill-dark)"/>
      <stop offset="0.22" style="stop-color: var(--fill-mid)"/>
      <stop offset="0.5" style="stop-color: var(--fill-light)"/>
      <stop offset="0.8" style="stop-color: var(--fill-mid)"/>
      <stop offset="1" style="stop-color: var(--fill-dark)"/>
    </linearGradient>
    <linearGradient id="trimGradient" x1="0" y1="1" x2="1" y2="0">
      <stop offset="0" style="stop-color: var(--trim-brown)"/>
      <stop offset="0.45" style="stop-color: var(--trim-copper)"/>
      <stop offset="0.7" style="stop-color: var(--trim-plum)"/>
      <stop offset="1" style="stop-color: var(--trim-gold)"/>
    </linearGradient>
  </defs>

  <!-- outer band -->
  <circle class="outer-band" cx="600" cy="599" r="598" fill="url(#ringGradient)"/>
  <!-- white hairline -->
  <circle class="hairline-ring" cx="600" cy="599" r="572" fill="none" stroke="var(--hairline)" stroke-width="4"/>
  <!-- inner field -->
  <circle class="inner-field" cx="600" cy="599" r="568" fill="url(#fillGradient)"/>
  <!-- metallic trim -->
  <circle class="trim-ring" cx="600" cy="599" r="543" fill="none" stroke="url(#trimGradient)" stroke-width="5"/>

  <!-- motto -->
  <text class="motto-lead" x="590" y="393" text-anchor="middle">Delicately</text>
  <text class="motto-line" x="598" y="522" text-anchor="middle">hand poured and infused</text>
  <text class="motto-line" x="588" y="632" text-anchor="middle">by me...for you</text>

  <!-- contact -->
  <text class="email-domain" x="910" y="782" text-anchor="end">@MAILBOX-DEMO.NET</text>
  <text class="email-user" x="600" y="864" text-anchor="middle">wickwillow</text>
  <text class="phone" x="590" y="976" text-anchor="middle">0487 913 072</text>
</svg>
</body>
</html>
```